Design some Business Cards for Gleaming Wheel Studio

I require some business cards to be design for my car detailing business "Gleaming Wheel Studio".

Preferred layout is landscape and artwork MUST be created in CMYK format and 300 dpi. Information that should be included is

Marcus Whitby
Vehicle Detailing Specialist

Tel: 07715 492 618
Email : marcus@gleamingwheelstudio.co.uk
Website : www.gleamingwheelstudio.co.uk

One side should have just the logo and maybe some design element - I have attached a example of a business card which I do like the black side with the image just visible behind the text (example.jpg). The other side should have all of the contact information and probably the logo on it too.

Plenty of images on my website if needed www.gleamingwheelstudio.co.uk

It should have a classy look to it and be very simple and stylish .

Please do not use any templates or clip art

```html
<!DOCTYPE html>
<html lang="en">
<head>
<meta charset="utf-8">
<title>Gleaming Wheel Studio — Business Cards</title>
<link rel="stylesheet" href="https://fonts.googleapis.com/css2?family=Arimo:wght@400;700&display=swap">
<style>
  :root {
    --backdrop: #2b2826;
    --card-core: #3a3a3a;
    --card-edge: #050505;
    --band: #ffffff;
    --accent: #6f8a3c;
    --accent-bright: #8fb04a;
    --ink-light: #f2f2f2;
    --ink-grey: #b9b9b9;
    --ink-dark: #2c3a14;
  }
  * { margin: 0; padding: 0; box-sizing: border-box; }
  html, body {
    width: 1200px; height: 960px; overflow: hidden;
    background: var(--backdrop);
    font-family: "Arimo", Arial, sans-serif;
  }
  .sheet { position: relative; width: 1200px; height: 960px; }
  .card {
    position: absolute; left: 220px;
    width: 760px; height: 434px;
    background: radial-gradient(ellipse at 50% 40%, var(--card-core) 0%, #151515 55%, var(--card-edge) 100%);
    box-shadow: 0 10px 30px rgba(0,0,0,0.5);
    overflow: hidden;
  }
  .card--front { top: 36px; }
  .card--back { top: 490px; }
  .card__band { position: absolute; inset: 0; }

  .brand {
    display: flex; align-items: center; gap: 10px;
    color: var(--ink-grey);
    font-weight: 400; text-transform: uppercase;
    letter-spacing: 0.22em;
  }
  .brand__mark { background: var(--ink-grey); flex: none; }

  .card--front .brand {
    position: absolute; left: 60px; top: 150px; font-size: 13px;
  }
  .card--front .brand__mark { width: 12px; height: 12px; }

  .contact {
    position: absolute; left: 62px; top: 312px;
    list-style: none;
  }
  .contact__item {
    display: flex; align-items: center; gap: 10px;
    color: var(--ink-light); font-size: 13px;
    height: 24px;
  }
  .contact__item:first-child { font-size: 16px; }
  .contact__icon {
    width: 15px; height: 15px; border-radius: 3px;
    background: var(--accent-bright);
    display: flex; align-items: center; justify-content: center; flex: none;
  }

  .card--back .brand {
    position: absolute; left: 50%; top: 50%;
    transform: translate(-50%, -50%);
    font-size: 22px; gap: 16px;
  }
  .card--back .brand__mark { width: 22px; height: 22px; }
</style>
</head>
<body>
<main class="sheet">

  <section class="card card--front" aria-label="Business card front">
    <svg class="card__band" width="760" height="434" viewBox="0 0 760 434">
      <polygon points="545,0 605,0 369,434 309,434" fill="var(--band)"/>
      <g transform="translate(457 217) rotate(-61.5)">
        <text class="band__name" x="0" y="2" text-anchor="middle"
              font-family="Arimo, Arial, sans-serif" font-weight="700" font-size="26"
              fill="var(--accent)">Marcus Whitby</text>
        <text class="band__title" x="0" y="19" text-anchor="middle"
              font-family="Arimo, Arial, sans-serif" font-weight="700" font-size="12"
              fill="var(--ink-dark)">Vehicle Detailing Specialist</text>
      </g>
    </svg>

    <div class="brand"><span class="brand__mark"></span>Gleaming Wheel Studio</div>

    <ul class="contact">
      <li class="contact__item">
        <span class="contact__icon">
          <svg width="9" height="9" viewBox="0 0 10 10"><path d="M2 1 L4 1 L4.8 3.2 L3.6 4 Q4.6 6 6 6.4 L6.8 5.2 L9 6 L9 8 Q8.5 9 7.5 9 Q1 8 1 2.5 Q1 1.3 2 1 Z" fill="#fff"/></svg>
        </span>07715 492 618
      </li>
      <li class="contact__item">
        <span class="contact__icon">
          <svg width="9" height="9" viewBox="0 0 10 10"><rect x="1" y="2.5" width="8" height="5.5" fill="none" stroke="#fff" stroke-width="1"/><path d="M1 2.5 L5 5.5 L9 2.5" fill="none" stroke="#fff" stroke-width="1"/></svg>
        </span>marcus@gleamingwheelstudio.co.uk
      </li>
      <li class="contact__item">
        <span class="contact__icon">
          <svg width="9" height="9" viewBox="0 0 10 10"><circle cx="5" cy="5" r="3.8" fill="none" stroke="#fff" stroke-width="1"/><path d="M1.2 5 H8.8 M5 1.2 Q2.8 5 5 8.8 M5 1.2 Q7.2 5 5 8.8" fill="none" stroke="#fff" stroke-width="0.8"/></svg>
        </span>www.gleamingwheelstudio.co.uk
      </li>
    </ul>
  </section>

  <section class="card card--back" aria-label="Business card back">
    <div class="brand"><span class="brand__mark"></span>Gleaming Wheel Studio</div>
  </section>

</main>
</body>
</html>
```